Lena Hartwell Web

Lena Hartwell is a singer/songwriter that has a presence in the market for over 20 years. She currently has a website, lenahartwell.example that needs a major makeover. IT needs to be reorganized to; 1) make it more user friendly; 2) enable multi-languages including; Spanish, French, Russian, Japanese, Chinese and Portuguese; 3) enable purchases online through a storefront of promotional merchandise and music tracks. She has a logo that needs an update, as well as we currently have a business card open on PixelBazaar for input. Working to re-brand, or refresh her brand.

Lena Hartwell is the next Rosa Delmont! She has 5 platinum records, Lumen Award nominations and tours with Harold Prescott globally and is Nora Vandermeer's key backup singer for 12 years.
Updates

Some common questions have come up.  Here is some further input:

1) Colors - No specific color in mind but probably earth tones.  Although at this point we''re completely open.  Mary likes classical style, Russian, French decor.  Paris architecture. Greek, Italian textures, Goddess like symbols from the Roman Empire, or the symbols and pomp of the British monarchy.  One name on tap for the new CD is "Lanterns Over Quiet Water"
2) Example website - I have not found a new one specifically, but what I don''t like about the existing one is it is not easy to navigate.  Needs to be streamlined and easy to navigate with a storefront for merchandise and music downloads.  
3) On Logo - We''re revamping a "Global" merchandise rollout logo.  We''ve also considered possibly modifying the old english "Hartwell" family crest which signifies royalty, but have not explored that too much.  The hexagon yellow logo on her current website, I was thinking of modifying to gold (brushed - or polished?), then taking the LH lettering using a fountain pen type look there the line thickness flows with pressure on the pen, then make the gold look like a pillow, with the letter making an impression into the gold pillow.  This expands to a high quality pin, blinged up broach with diamonds imbedded for example, Global label identity, tee shirts, label tag on fashion clothing etc etc. 
 4) One thing marketing has asked us to build is a routine video blog to reach out to fans in a personal way.  Short clips of daily activity, travel prep for shows, etc. Possibly a signup/fanpage where people get emails sent back whenever anything new is posted, like a video blog, new pics, new events.  A menu to choose what you get updates on. 

Thanks, Dennis

Target Market(s)

1) Fan base in Europe, Asia, Latin America and North America
2) Movie producers seeking soundtracks
3) Private clients seeking an outstanding performer for corporate events

Industry/Entity Type

Singer

Requirements
Must have
• Better organization into smaller pages. Items critical include: 1) music tracks, 2) ClipStream links, 3) photos & Video, 4) storefront to enable online merchandise purchase 5) a way to illustrate her genre from; gospel, to rock, funk, R&B, country,

```html
<!DOCTYPE html>
<html lang="en">
<head>
<meta charset="utf-8">
<title>Lena Hartwell — Singer &amp; Songwriter</title>
<link rel="stylesheet" href="https://fonts.googleapis.com/css2?family=Arimo:wght@400;700&family=Julius+Sans+One&family=Oswald:wght@400;500&display=swap">
<style>
:root{
  --bg-top:#161616;
  --bg-mid:#2a2a2a;
  --bg-foot:#121212;
  --panel:#0c0c0c;
  --yellow:#f5d327;
  --orange:#f08a24;
  --white:#ffffff;
  --text:#d8d8d8;
  --muted:#8a8a8a;
  --line:#4a4a4a;
  --teal:#2fc6c6;
}
*{margin:0;padding:0;box-sizing:border-box}
html,body{width:1129px;height:1200px;overflow:hidden}
body{position:relative;background:var(--bg-mid);font-family:"Arimo",Arial,sans-serif;color:var(--text)}
.abs{position:absolute}
.nw{white-space:nowrap}
.band-top{left:0;top:0;width:1129px;height:354px;background:var(--bg-top)}
.band-foot{left:0;top:1123px;width:1129px;height:77px;background:var(--bg-foot)}

.brand{left:450px;top:20px;width:240px;height:50px}
.brand-mark{left:0;top:2px;width:40px;height:40px;background:var(--yellow)}
.brand-name{left:56px;top:8px;font-family:"Julius Sans One",sans-serif;font-size:23px;color:var(--yellow);letter-spacing:2px;white-space:nowrap}
.brand-tag{left:92px;top:36px;font-size:11px;color:var(--white);white-space:nowrap}
.brand-tag i{display:inline-block;width:6px;height:6px;border-radius:50%;background:var(--yellow);margin:0 6px 1px}

.nav{left:266px;top:109px;width:615px;height:39px;background:var(--panel)}
.nav a{position:absolute;top:15px;font-size:7.5px;color:#bbb;text-decoration:none;letter-spacing:.3px}
.nav a.active{color:var(--yellow)}
.nav .active-bar{position:absolute;left:90px;top:-1px;width:43px;height:2px;background:var(--yellow)}

.hero{left:266px;top:148px;width:615px;height:228px;background:linear-gradient(100deg,#6b4a32 0%,#a8713f 35%,#3b2a22 55%,#b07a44 75%,#6d4a2c 100%)}
.hero-badge{left:810px;top:300px;width:40px;height:40px;background:var(--yellow)}
.hero-dots{left:807px;top:356px;display:flex;gap:4px}
.hero-dots span{width:7px;height:7px;border-radius:50%;background:#222}
.hero-dots span:first-child{background:var(--yellow)}

.heading{font-family:"Oswald",sans-serif;font-weight:400;font-size:21px;color:var(--white);white-space:nowrap}
.rule{height:1px;background:var(--line)}
.lead{font-size:9.5px;font-weight:700;color:var(--white);line-height:15px;white-space:nowrap}
.body-s{font-size:7.5px;color:var(--muted);line-height:12px}
.btn-ghost{border:1px solid #666;color:#aaa;font-size:7.5px;display:flex;align-items:center;justify-content:center}

.about-photo{left:499px;top:444px;width:114px;height:113px;background:linear-gradient(180deg,#3a4554 0%,#8a6a55 45%,#a0302e 70%,#b8a58e 100%)}

.promo{left:266px;top:580px;width:615px;height:66px;background:var(--white);text-align:center}
.promo-title{position:absolute;left:0;right:0;top:16px;font-family:"Oswald",sans-serif;font-size:18px;color:#222}
.promo-title b{color:var(--orange);font-weight:500}
.promo-sub{position:absolute;left:0;right:0;top:40px;font-size:10px;color:var(--muted)}

.tour{left:266px;top:646px;width:615px;height:180px;background:var(--panel)}
.date-day{font-size:22px;font-weight:700;color:var(--white)}
.date-mon{font-size:11px;font-weight:700;color:var(--white)}
.event-title{font-size:8.5px;font-weight:700;color:var(--yellow);white-space:nowrap}
.upcoming{font-size:12px;font-weight:700;color:var(--white);line-height:15px}
.upcoming b{color:var(--yellow)}

.ev-date{font-family:"Oswald",sans-serif;font-size:16px;color:var(--yellow)}
.ev-title{font-size:7.5px;font-weight:700;color:var(--white)}
.dl-list{list-style:none}
.dl-list li{height:14.6px;font-size:7px;font-weight:700;color:#ccc;display:flex;align-items:center;white-space:nowrap}
.dl-list li::before{content:"";width:7px;height:7px;border-radius:50%;border:1px solid #666;margin-right:9px;margin-left:-16px}
.own{font-size:9px;color:var(--yellow)}
.own-links{font-size:6.5px;color:var(--yellow);white-space:nowrap}
.btn-order{left:442px;top:1045px;width:70px;height:21px;background:var(--yellow);color:#222;font-size:9px;display:flex;align-items:center;justify-content:center}
.web-thumb{width:86px;height:61px}
.web-title{font-size:8.5px;font-weight:700;color:var(--white);line-height:11px;white-space:nowrap}
.web-body{font-size:7px;color:var(--muted);line-height:9px;white-space:nowrap}
.ev-body{font-size:7px;color:var(--muted);line-height:10px;white-space:nowrap}

.social{left:266px;top:1159px;display:flex;gap:3px}
.social span{width:24px;height:24px;background:#3a3a3a;color:#ddd;font-size:6px;display:flex;align-items:center;justify-content:center}
.foot-on{left:442px;top:1160px;font-size:7px;color:#ccc}
.foot-wave{left:500px;top:1157px;font-size:9px;font-weight:700;color:var(--orange)}
.foot-line{left:442px;top:1176px;font-size:7.5px;color:var(--white);font-weight:700;white-space:nowrap}
.foot-line b{color:var(--teal)}
</style>
</head>
<body>
<div class="abs band-top"></div>
<div class="abs band-foot"></div>

<header class="abs brand">
  <div class="abs brand-mark"></div>
  <div class="abs brand-name">Lena Hartwell</div>
  <div class="abs brand-tag">singer<i></i>songwriter</div>
</header>

<nav class="abs nav">
  <span class="active-bar"></span>
  <a class="active" style="left:102px">HOME</a>
  <a style="left:150px">EVENTS</a>
  <a style="left:197px">MUSIC</a>
  <a style="left:244px">VIDEOS</a>
  <a style="left:289px">PICTURES</a>
  <a style="left:350px">ABOUT</a>
  <a style="left:396px">DISCOGRAPHY</a>
  <a style="left:466px">CONTACT</a>
</nav>

<div class="abs hero" role="img" aria-label="Portrait of Lena Hartwell seated in a car with tan leather seats, wearing a fur collar"></div>
<div class="abs hero-badge"></div>
<div class="abs hero-dots"><span></span><span></span><span></span><span></span><span></span></div>

<section>
  <h2 class="abs heading" style="left:266px;top:396px">HI EVERYONE</h2>
  <div class="abs rule" style="left:266px;top:432px;width:180px"></div>
  <p class="abs lead" style="left:267px;top:441px">Lorem ipsum dolor sit amet, consectetur<br>adipisicing elit, sed do eiusmod</p>
  <p class="abs body-s nw" style="left:267px;top:476px">Lorem ipsum dolor sit amet, consectetur adipisicing<br>elit, sed do eiusmod tempor incididunt ut labore et<br>dolore magna aliqua. Ut enim ad minim veniam</p>
  <div class="abs btn-ghost" style="left:266px;top:533px;width:69px;height:25px">READ MORE</div>
</section>

<section>
  <h2 class="abs heading" style="left:499px;top:396px">A FEW WORDS ABOUT ME</h2>
  <div class="abs rule" style="left:499px;top:432px;width:382px"></div>
  <div class="abs about-photo" role="img" aria-label="Lena Hartwell standing in a long red gown"></div>
  <p class="abs nw" style="left:629px;top:443px;font-size:11px;font-weight:700;color:var(--white)">Lorem ipsum dolor sit amet</p>
  <p class="abs body-s nw" style="left:629px;top:476px;font-size:7px">Lorem ipsum dolor sit amet, consectetur adipisicing elit, sed do eiusmod tempor<br>incididunt ut labore et dolore magna aliqua. Ut enim ad minim veniam, quis nos-<br>trud exercitation ullamco laboris nisi ut aliquip ex ea commodo consequat.</p>
  <div class="abs btn-ghost" style="left:629px;top:533px;width:68px;height:25px">READ MORE</div>
</section>

<section class="abs promo">
  <svg class="abs" style="left:20px;top:24px" width="10" height="18" viewBox="0 0 10 18"><path d="M9 1 1 9l8 8" fill="none" stroke="#ccc" stroke-width="1.2"/></svg>
  <svg class="abs" style="left:585px;top:24px" width="10" height="18" viewBox="0 0 10 18"><path d="M1 1l8 8-8 8" fill="none" stroke="#ccc" stroke-width="1.2"/></svg>
  <div class="promo-title"><b>APRIL 24</b> - NEW PROMO LOREM IPSUM</div>
  <div class="promo-sub">Lorem ipsum dolor sit amet, consectetur adipisicing elit, sed do eiusmod tempor</div>
</section>

<section class="abs tour">
  <div class="abs date-day" style="left:29px;top:40px">29</div>
  <div class="abs date-mon" style="left:29px;top:64px">MAY</div>
  <div class="abs event-title" style="left:29px;top:94px">LOREM IPSUM DOLORE MASSA AS TUM</div>
  <p class="abs body-s nw" style="left:29px;top:117px">Ut enim ad minim veniam, quis nostrud exercitation<br>ullamcode laboris nisi dolore massa. Etaliquipx eato<br>commodo conse cupiditate non.</p>
  <div class="abs date-day" style="left:261px;top:40px">05</div>
  <div class="abs date-mon" style="left:261px;top:64px">JUN</div>
  <div class="abs event-title" style="left:261px;top:94px">LOREM IPSUM DOLORE MASSA AS TUM</div>
  <p class="abs body-s nw" style="left:261px;top:117px">Ut enim ad minim veniam, quis nostrud exercitation<br>ullamcode laboris nisi dolore massa. Etaliquipx eato<br>commodo conse cupiditate non.</p>
  <div class="abs upcoming" style="left:498px;top:73px">UPCOMING<br><b>TOUR</b> DATE</div>
  <div class="abs btn-ghost" style="left:497px;top:111px;width:69px;height:24px">VIEW DETAIL</div>
</section>

<section>
  <h2 class="abs heading" style="left:266px;top:845px;font-size:17px">LATEST EVENT</h2>
  <div class="abs ev-date" style="left:267px;top:886px">09.03.2014</div>
  <div class="abs ev-title" style="left:267px;top:915px">Lorem ipsum dolor</div>
  <p class="abs ev-body" style="left:267px;top:932px">Lorem ipsum dolor sit amet, consect-<br>etur adipisicing elit, sed do eiusmod</p>
  <div class="abs rule" style="left:266px;top:965px;width:121px"></div>
  <div class="abs ev-date" style="left:267px;top:976px">09.03.2014</div>
  <div class="abs ev-title" style="left:267px;top:1005px">Lorem ipsum dolor</div>
  <p class="abs ev-body" style="left:267px;top:1022px">Lorem ipsum dolor sit amet, consect-<br>etur adipisicing elit, sed do eiusmod</p>
  <div class="abs rule" style="left:266px;top:1055px;width:121px"></div>
  <div class="abs btn-ghost" style="left:266px;top:1079px;width:69px;height:24px">MORE EVENTS</div>
</section>

<section>
  <h2 class="abs heading" style="left:441px;top:845px;font-size:17px">DOWNLOAD MUSIC</h2>
  <ul class="abs dl-list" style="left:457px;top:890px">
    <li>Lorem ipsum dolor amet</li>
    <li>Lorem ipsum dolor sit amet</li>
    <li>Lorem ipsum dolor</li>
    <li>Lorem ipsum dolor sit amet</li>
    <li>Lorem ipsum</li>
    <li>Lorem ipsum dolor sit amet</li>
    <li>Lorem ipsum sit amet</li>
  </ul>
  <div class="abs own" style="left:442px;top:1016px">Own This Series</div>
  <div class="abs own-links" style="left:442px;top:1030px">Tuneshelf | ClipStream | VIDEO | Music</div>
  <div class="abs btn-order">ORDER NOW</div>
</section>

<section>
  <h2 class="abs heading" style="left:634px;top:845px;font-size:17px">FROM THE WEB</h2>
  <div class="abs web-thumb" style="left:634px;top:892px;background:linear-gradient(135deg,#3a1a4a,#8a3a6a 60%,#2a1030)" role="img" aria-label="Lena Hartwell performing on stage"></div>
  <p class="abs web-title" style="left:730px;top:890px">Lorem ipsum dolor sit amet, consect-<br>etur adipisicing</p>
  <p class="abs web-body" style="left:730px;top:914px">Lorem ipsum dolor sit amet, consectetur adipisicing<br>elit, sed do eiusmod tempor</p>
  <div class="abs web-thumb" style="left:634px;top:967px;background:linear-gradient(180deg,#3a4554,#8a6a55 50%,#a0302e 80%,#b8a58e)" role="img" aria-label="Lena Hartwell in a red gown"></div>
  <p class="abs web-title" style="left:730px;top:966px">Lorem ipsum dolor sit amet</p>
  <p class="abs web-body" style="left:730px;top:979px">Lorem ipsum dolor sit amet, consectetur adipisicing<br>elit, sed do eiusmod tempor</p>
  <div class="abs web-thumb" style="left:634px;top:1043px;background:linear-gradient(180deg,#3a4554,#8a6a55 50%,#a0302e 80%,#b8a58e)" role="img" aria-label="Lena Hartwell in a red gown"></div>
  <p class="abs web-title" style="left:730px;top:1041px">Lorem ipsum</p>
  <p class="abs web-body" style="left:730px;top:1054px">Lorem ipsum dolor sit amet, consectetur adipisicing<br>elit, sed do eiusmod tempor</p>
</section>

<footer>
  <div class="abs social"><span>Kin</span><span>Peep</span><span>Guild</span><span>Loop</span><span>Feed</span></div>
  <div class="abs foot-on">Lena Hartwell On</div>
  <div class="abs foot-wave">WaveCove</div>
  <div class="abs foot-line"><b>Tonight on Brightime</b> &nbsp;9.00 pm NOVA WORLD &nbsp;<b>|</b>&nbsp; 10.00am &nbsp;NOVA GOLD</div>
</footer>
</body>
</html>
```